Business Card Design

We are an IT staffing and consulting company providing IT solutions and resources to our clients.

Industry/Entity Type

Business

Contact Information for Business Card

Ramesh Tulavarthi
Vice President

BrightNode Inc
48215 Harrowmere Court Square, suite 700
Ashburn, VA 20147
Direct: 571-555-0193
Mobile: 571-555-0147
Email: Ramesh@brightnodeinc.com
Fax: 703-555-0162
www.brightnodeinc.com

```html
<!DOCTYPE html>
<html lang="en">
<head>
<meta charset="utf-8">
<title>BrightNode Inc – Business Card</title>
<link rel="stylesheet" href="https://fonts.googleapis.com/css2?family=Mulish:wght@400;700&display=swap">
<style>
  :root {
    --brand-red: #c0212f;
    --ink: #1f1f1f;
    --paper: #ffffff;
    --backdrop: #e9e6e2;
    --card-shadow: 0 4px 14px rgba(0, 0, 0, 0.22);
  }
  * { box-sizing: border-box; margin: 0; padding: 0; }
  html, body {
    width: 1200px;
    height: 1000px;
    overflow: hidden;
  }
  body {
    background: var(--backdrop);
    font-family: "Mulish", sans-serif;
    position: relative;
  }
  .card {
    position: absolute;
    left: 265px;
    width: 666px;
    height: 397px;
    box-shadow: var(--card-shadow);
  }
  .card--front { top: 73px; background: var(--paper); }
  .card--back { top: 532px; background: var(--brand-red); }

  /* Front: brand name in place of the mark */
  .front-brand {
    position: absolute;
    left: 48px;
    top: 170px;
    display: flex;
    align-items: center;
    gap: 10px;
    color: var(--brand-red);
    font-weight: 700;
    font-size: 30px;
    letter-spacing: 0.5px;
  }
  .brand-dot {
    width: 14px;
    height: 14px;
    border-radius: 50%;
    background: currentColor;
  }

  .contact {
    position: absolute;
    left: 333px;
    top: 79px;
    color: var(--ink);
    font-size: 16.5px;
    line-height: 21px;
  }
  .contact__name {
    color: var(--brand-red);
    font-weight: 700;
    font-size: 19px;
    line-height: 24px;
  }
  .contact__title { margin-bottom: 14px; }
  .contact__list { list-style: none; }
  .contact__list li {
    display: flex;
    align-items: center;
    gap: 7px;
    height: 21.5px;
  }
  .icon {
    width: 13px;
    height: 13px;
    flex: none;
    fill: var(--brand-red);
  }
  .contact__company {
    color: var(--brand-red);
    margin-top: 4px;
    line-height: 22px;
  }
  .contact__address { line-height: 23px; }

  /* Back */
  .back-brand {
    position: absolute;
    left: 0;
    right: 0;
    top: 168px;
    display: flex;
    justify-content: center;
    align-items: center;
    gap: 14px;
    color: var(--paper);
    font-weight: 700;
    font-size: 50px;
    letter-spacing: 1px;
  }
  .back-brand .brand-dot { width: 22px; height: 22px; }
  .back-url {
    position: absolute;
    left: 0;
    right: 0;
    top: 348px;
    text-align: center;
    color: var(--paper);
    font-size: 16px;
    letter-spacing: 1.6px;
  }
  .back-url strong { font-weight: 700; }
</style>
</head>
<body>

<section class="card card--front" aria-label="Business card front">
  <div class="front-brand"><span class="brand-dot"></span>BrightNode</div>

  <div class="contact">
    <p class="contact__name">Ramesh Tulavarthi</p>
    <p class="contact__title">Vice President</p>
    <ul class="contact__list">
      <li>
        <svg class="icon" viewBox="0 0 16 16" aria-hidden="true"><path d="M4.5 0h7A1.5 1.5 0 0 1 13 1.5v13a1.5 1.5 0 0 1-1.5 1.5h-7A1.5 1.5 0 0 1 3 14.5v-13A1.5 1.5 0 0 1 4.5 0zm.5 2v10h6V2zm3 11a1 1 0 1 0 0 2 1 1 0 0 0 0-2z"/></svg>
        571-555-0147
      </li>
      <li>
        <svg class="icon" viewBox="0 0 16 16" aria-hidden="true"><path d="M1 5c0-2 3-3 7-3s7 1 7 3v1.5h-3.5V5h-7v1.5H1zm3 2h8l3 4v4H1v-4zm4 2a2 2 0 1 0 0 4 2 2 0 0 0 0-4z"/></svg>
        571-555-0193
      </li>
      <li>
        <svg class="icon" viewBox="0 0 16 16" aria-hidden="true"><path d="M4 0h8v5H4zM1 6h14v7h-3v3H4v-3H1zm4 5v3h6v-3zm7-3a1 1 0 1 0 0 2 1 1 0 0 0 0-2z"/></svg>
        703-555-0162
      </li>
      <li>
        <svg class="icon" viewBox="0 0 16 16" aria-hidden="true"><path d="M0 3h16v1.2L8 9 0 4.2zm0 2.8 8 4.8 8-4.8V13H0z"/></svg>
        Ramesh@brightnodeinc.com
      </li>
      <li>
        <svg class="icon" viewBox="0 0 16 16" aria-hidden="true"><path d="M8 0a8 8 0 1 0 0 16A8 8 0 0 0 8 0zm-1 1.6V5H4.2A6.5 6.5 0 0 1 7 1.6zm2 0A6.5 6.5 0 0 1 11.8 5H9zM1.6 7H7v2H1.6a6.4 6.4 0 0 1 0-2zM9 7h5.4a6.4 6.4 0 0 1 0 2H9zm-4.8 4H7v3.4A6.5 6.5 0 0 1 4.2 11zM9 11h2.8A6.5 6.5 0 0 1 9 14.4z"/></svg>
        www.brightnodeinc.com
      </li>
    </ul>
    <p class="contact__company">BrightNode Inc</p>
    <p class="contact__address">48215 Harrowmere Court Square,<br>suite 700 Ashburn, VA 20147</p>
  </div>
</section>

<section class="card card--back" aria-label="Business card back">
  <div class="back-brand"><span class="brand-dot"></span>BrightNode</div>
  <p class="back-url">www.<strong>brightnodeinc</strong>.com</p>
</section>

</body>
</html>
```